KORBALT

The business want a professional looking business card. We have a scetch we will add but want the extra upgrade, and would like more suggestions for variations of our business cards.

```html
<!DOCTYPE html>
<html lang="en">
<head>
<meta charset="UTF-8">
<title>KORBALT – Business Card</title>
<link rel="stylesheet" href="https://fonts.googleapis.com/css2?family=Federo&family=Marcellus&family=Poppins:wght@400;500&display=swap">
<style>
  :root {
    --backdrop: #d4d4d4;
    --card-light: #f0f0f0;
    --navy: #0f3347;
    --gold-light: #e6d07a;
    --gold: #b8924a;
    --gold-deep: #8c5714;
    --ink: #555555;
    --cream: #e4dbbd;
  }
  * { margin: 0; padding: 0; box-sizing: border-box; }
  html, body { width: 1200px; height: 1200px; overflow: hidden; }
  body { background: var(--backdrop); position: relative; font-family: "Poppins", sans-serif; }

  .card { position: absolute; width: 732px; height: 418px; }
  .card-front { left: 235px; top: 153px; background: var(--card-light); }
  .card-back { left: 233px; top: 629px; background: var(--navy); }

  .person-icon { position: absolute; left: 50px; top: 70px; width: 24px; height: 23px; }
  .holder-title {
    position: absolute; left: 89px; top: 62px;
    font-family: "Federo", sans-serif; font-size: 41px; line-height: 1; letter-spacing: 0.5px;
    background: linear-gradient(180deg, var(--gold-light), var(--gold) 55%, var(--gold-deep));
    -webkit-background-clip: text; background-clip: text; color: transparent;
    white-space: nowrap;
  }
  .title-rule { position: absolute; left: 89px; top: 103px; width: 191px; height: 1.5px; background: var(--navy); }
  .role { position: absolute; left: 89px; top: 110px; font-size: 12px; color: var(--ink); }
  .holder-name { position: absolute; left: 89px; top: 124px; font-size: 17px; color: var(--ink); }
  .divider-thick { position: absolute; left: 52px; top: 163px; width: 304px; height: 7px; background: var(--navy); }
  .divider-thin { position: absolute; left: 356px; top: 165px; width: 321px; height: 2px; background: var(--navy); }

  .contact-list { position: absolute; left: 52px; top: 233px; list-style: none; }
  .contact-item { display: flex; align-items: center; height: 22px; margin-bottom: 22px; font-size: 20px; color: var(--ink); }
  .contact-item svg { width: 20px; height: 20px; margin-right: 16px; flex: none; }

  .front-brand { position: absolute; left: 505px; top: 214px; width: 160px; text-align: center; }
  .brand-dot { display: block; margin: 0 auto 12px; width: 52px; height: 52px; border-radius: 50%; background: var(--gold); }
  .front-brand .brand-name { font-family: "Marcellus", serif; font-size: 26px; letter-spacing: 4px; color: var(--gold); }

  .back-brand { position: absolute; left: 0; right: 0; top: 140px; text-align: center; }
  .back-brand .brand-dot { width: 72px; height: 72px; margin-bottom: 30px; }
  .back-brand .brand-name { font-family: "Marcellus", serif; font-size: 40px; line-height: 1; letter-spacing: 12px; padding-left: 12px; color: var(--cream); }
  .tagline { margin-top: 10px; font-size: 12px; font-weight: 500; letter-spacing: 6px; padding-left: 6px; color: var(--cream); }
</style>
</head>
<body>
  <section class="card card-front">
    <svg class="person-icon" viewBox="0 0 24 23" aria-hidden="true">
      <defs><linearGradient id="goldV" x1="0" y1="0" x2="0" y2="1"><stop offset="0" stop-color="#e6d07a"/><stop offset="1" stop-color="#a77a32"/></linearGradient></defs>
      <circle cx="12" cy="6" r="5" fill="url(#goldV)"/>
      <path d="M0 23 C1 15 6 12.5 12 12.5 S23 15 24 23 Z" fill="url(#goldV)"/>
    </svg>
    <h1 class="holder-title">KORBALT H MOLDVIK</h1>
    <div class="title-rule"></div>
    <p class="role">CEO &amp; Founder</p>
    <p class="holder-name">Lars Henrik Moldvik</p>
    <div class="divider-thick"></div>
    <div class="divider-thin"></div>

    <ul class="contact-list">
      <li class="contact-item">
        <svg viewBox="0 0 20 20" aria-hidden="true"><path d="M4 1.5 L7 5.5 L5.5 7.5 C6.5 10 9.5 13 12.5 14.5 L14.5 13 L18.5 16 L16.5 18.5 C9 18 2 11 1.5 3.5 Z" fill="#b8924a"/></svg>
        +004791530764
      </li>
      <li class="contact-item">
        <svg viewBox="0 0 20 20" aria-hidden="true"><rect x="0.5" y="4" width="19" height="12" fill="#c9a55a"/><path d="M0.5 4 L10 11 L19.5 4 M0.5 16 L7.5 9.5 M19.5 16 L12.5 9.5" stroke="#f0f0f0" stroke-width="1.2" fill="none"/></svg>
        korbalt.llc@postline.com
      </li>
      <li class="contact-item">
        <svg viewBox="0 0 20 20" aria-hidden="true"><g fill="none" stroke="#b8924a" stroke-width="1.3"><circle cx="10" cy="10" r="8.5"/><ellipse cx="10" cy="10" rx="3.8" ry="8.5"/><path d="M1.5 10 H18.5 M3 5.5 H17 M3 14.5 H17 M10 1.5 V18.5"/></g></svg>
        www.korbalt.llc
      </li>
    </ul>

    <div class="front-brand">
      <span class="brand-dot"></span>
      <p class="brand-name">KORBALT</p>
    </div>
  </section>

  <section class="card card-back">
    <div class="back-brand">
      <span class="brand-dot"></span>
      <p class="brand-name">KORBALT</p>
      <p class="tagline">SINCE 2026</p>
    </div>
  </section>
</body>
</html>
```